Announcement Card

This will be an announcement card mailed to clients as a postcard. The text should be oriented book fashion (not landscape).

Text is:

DEREK T. HOLLOWAN

is pleased to announce
he is joining

BRIARCREST LAW GROUP

as a founding partner

[PHONE, ADDRESS, EMAIL]

Industry/Entity Type

Fashion

```html
<!DOCTYPE html>
<html lang="en">
<head>
<meta charset="utf-8">
<title>Announcement Card — Derek T. Hollowan</title>
<link rel="stylesheet" href="https://fonts.googleapis.com/css2?family=Crimson+Text:wght@400&family=Pinyon+Script&display=swap">
<style>
  :root {
    --paper: #ffffff;
    --ink: #1c1c1c;
  }
  html, body {
    margin: 0;
    padding: 0;
    overflow: hidden;
    background: var(--paper);
  }
  .card {
    position: relative;
    width: 924px;
    height: 1200px;
    background: var(--paper);
    color: var(--ink);
    overflow: hidden;
  }
  .line {
    position: absolute;
    left: 0;
    width: 100%;
    margin: 0;
    text-align: center;
    line-height: 1;
    white-space: nowrap;
  }
  .serif {
    font-family: "Crimson Text", Georgia, serif;
    font-weight: 400;
    font-variant-numeric: oldstyle-nums;
    font-size: 70px;
  }
  .script {
    font-family: "Pinyon Script", "Brush Script MT", cursive;
    font-size: 38px;
  }
  .name        { top: 100px; }
  .intro-one   { top: 240px; }
  .intro-two   { top: 318px; }
  .firm        { top: 428px; }
  .role        { top: 572px; }
  .phone       { top: 672px; }
  .street      { top: 786px; }
  .city        { top: 900px; }
  .email       { top: 1006px; }
</style>
</head>
<body>
  <main class="card">
    <h1 class="line serif name">Derek T. Hollowan</h1>
    <p class="line script intro-one">is pleased to announce</p>
    <p class="line script intro-two">he is joining</p>
    <h2 class="line serif firm">Briarcrest Law Group</h2>
    <p class="line script role">as a founding partner</p>
    <p class="line serif phone">000-000-0000</p>
    <p class="line serif street">418 Alder Lane</p>
    <p class="line serif city">New York, NY 10027</p>
    <p class="line serif email">dth@briarmail.com</p>
  </main>
</body>
</html>
```